Lucien business card

Business card for commercial photography , photographer specialized in advertising, architecture and interior photography, adventure imagery and camera work. 40 years old, worked for the last 20 years. Business card needs to convey a sense of confidence in work achieved. Card needs to be eye catching as will be left behind in many people's offices. Should also mention discreetly NRVB accredited photographer at the verso of the card. Phone number and website link must be apparent easily.

Target Market(s)

Advertising agencies, commercial photography representation

Industry/Entity Type

Architecture

Contact Information for Business Card

Phone number : +61 470 918 264
lucien.marvaux@velmora.example
www.lucienmarvaux.example

Font styles to use
Sans Serif

Requirements
Must have
• Email adress
• Website
• Phone number
• Name
• Photographer
Nice to have
• NRVB accredited photographer
Should not have
• Rond corners

```html
<!DOCTYPE html>
<html lang="en">
<head>
<meta charset="utf-8">
<title>Lucien business card</title>
<link rel="stylesheet" href="https://fonts.googleapis.com/css2?family=Archivo+Black&family=Arimo:wght@400&family=Barlow+Condensed:wght@300&family=Cinzel:wght@600&display=swap">
<style>
  :root {
    --ink: #000000;
    --paper: #ffffff;
    --accent: #ff8540;
    --badge: #222222;
  }
  html, body {
    margin: 0;
    padding: 0;
    width: 1000px;
    height: 1200px;
    overflow: hidden;
    background: var(--paper);
  }
  .canvas {
    position: relative;
    width: 1000px;
    height: 1200px;
  }
  .card {
    position: absolute;
    left: 20px;
    width: 957px;
    height: 557px;
  }
  .card--front { top: 16px; }
  .card--back { top: 626px; }
  .card svg {
    position: absolute;
    inset: 0;
    width: 100%;
    height: 100%;
  }
  .frame-bar { fill: var(--ink); }
  .mark-text {
    font-family: "Archivo Black", "Arial Black", sans-serif;
  }
  .mark-text--accent { fill: var(--accent); }
  .mark-text--ink { fill: var(--ink); }
  .rule--accent { fill: var(--accent); }
  .rule--ink { fill: var(--ink); }

  .back-name {
    position: absolute;
    left: 0;
    width: 1000px;
    top: 740px;
    margin: 0;
    text-align: center;
    font-family: "Barlow Condensed", "Arial Narrow", sans-serif;
    font-weight: 300;
    font-size: 52px;
    line-height: 52px;
    letter-spacing: 2px;
    color: var(--ink);
  }
  .back-role {
    position: absolute;
    left: 347px;
    top: 800px;
    width: 304px;
    height: 35px;
    margin: 0;
    background: var(--ink);
    color: var(--paper);
    text-align: center;
    font-family: "Cinzel", serif;
    font-weight: 600;
    font-size: 27px;
    line-height: 36px;
    letter-spacing: 2px;
  }
  .contact-row {
    position: absolute;
    left: 265px;
    height: 30px;
    margin: 0;
    white-space: nowrap;
  }
  .contact-row--email { top: 906px; }
  .contact-row--web { top: 951px; }
  .contact-row--phone { top: 995px; }
  .contact-label,
  .contact-colon {
    position: absolute;
    font-family: "Arimo", Arial, sans-serif;
    font-size: 26px;
    line-height: 30px;
    color: var(--accent);
  }
  .contact-label { left: 0; }
  .contact-colon { left: 96px; }
  .contact-value {
    position: absolute;
    left: 116px;
    font-family: "Barlow Condensed", "Arial Narrow", sans-serif;
    font-weight: 300;
    font-size: 29px;
    line-height: 30px;
    letter-spacing: 1.2px;
    color: var(--ink);
  }
  .accreditation-badge {
    position: absolute;
    left: 817px;
    top: 1009px;
    width: 120px;
    height: 120px;
    border-radius: 50%;
    background: var(--badge);
  }
</style>
</head>
<body>
<main class="canvas">

  <section class="card card--front" aria-label="Card front">
    <svg viewBox="0 0 1076 626" xmlns="http://www.w3.org/2000/svg">
      <rect class="frame-bar" x="24" y="0" width="1028" height="24"/>
      <rect class="frame-bar" x="0" y="24" width="24" height="578"/>
      <rect class="frame-bar" x="1052" y="24" width="24" height="578"/>
      <rect class="frame-bar" x="24" y="602" width="1028" height="24"/>

      <rect class="rule--accent" x="190" y="170" width="14" height="270"/>
      <text class="mark-text mark-text--ink" font-size="112" x="236" y="292">Lucien</text>
      <text class="mark-text mark-text--accent" font-size="112" x="236" y="412">Marvaux</text>
      <rect class="rule--ink" x="236" y="432" width="640" height="8"/>
    </svg>
  </section>

  <section class="card card--back" aria-label="Card back">
    <svg viewBox="0 0 1076 626" xmlns="http://www.w3.org/2000/svg">
      <rect class="frame-bar" x="24" y="0" width="1028" height="24"/>
      <rect class="frame-bar" x="0" y="24" width="24" height="578"/>
      <rect class="frame-bar" x="1052" y="24" width="24" height="578"/>
      <rect class="frame-bar" x="24" y="602" width="1028" height="24"/>
    </svg>
  </section>

  <h1 class="back-name">LUCIEN MARVAUX</h1>
  <p class="back-role">PHOTOGRAPHER</p>

  <p class="contact-row contact-row--email">
    <span class="contact-label">email</span><span class="contact-colon">:</span><span class="contact-value">lucien.marvaux@velmora.example</span>
  </p>
  <p class="contact-row contact-row--web">
    <span class="contact-label">website</span><span class="contact-colon">:</span><span class="contact-value">www.lucienmarvaux.example</span>
  </p>
  <p class="contact-row contact-row--phone">
    <span class="contact-label">phone</span><span class="contact-colon">:</span><span class="contact-value">+61 470 918 264</span>
  </p>

  <div class="accreditation-badge" role="img" aria-label="NRVB accredited photographer badge"></div>

</main>
</body>
</html>
```